Looking for a modern, Professional business card design

We have a simple business card, but are looking for a more modern, professional look. A sample of the basic card is attached as well as the logo. We would also like to add that we offer:
Struggling with your finances?
- Learn to become debt free
- Discover the power of cash
- Control your money instead of it controlling you
Let us help you achieve a new level of financial freedom!
Also, we would like to have a "SPECIAL OFFER!: FREE 30 minute consultation"
Financial Planning

```html
<!DOCTYPE html>
<html lang="en">
<head>
<meta charset="utf-8">
<title>Lantern Financial Coaching – Business Card</title>
<link href="https://fonts.googleapis.com/css2?family=Source+Sans+3:ital,wght@0,400;0,600;0,700;1,400;1,600&display=swap" rel="stylesheet">
<style>
  :root {
    --page: #e9e6e4;
    --card-top: #f3f1f0;
    --brand-green: #2e7d3a;
    --brand-dark: #1f1f1f;
    --ink: #2a2a2a;
    --white: #ffffff;
    --accent-green: #5cb848;
  }
  * { box-sizing: border-box; margin: 0; padding: 0; }
  html, body {
    width: 1200px; height: 900px; overflow: hidden;
    background: var(--page);
    font-family: "Source Sans 3", Arial, sans-serif;
  }
  .canvas { position: relative; width: 1200px; height: 900px; }

  .card {
    position: absolute;
    width: 556px; height: 342px;
    background: var(--card-top);
    box-shadow: 0 6px 18px rgba(0,0,0,0.18);
    overflow: hidden;
  }
  .card--front { left: 238px; top: 62px; }
  .card--back  { left: 457px; top: 519px; width: 560px; }

  /* brand lockup */
  .brand {
    position: absolute; left: 130px; top: 72px;
    display: flex; align-items: center; gap: 14px;
  }
  .brand__dot {
    width: 34px; height: 34px; border-radius: 50%;
    background: var(--accent-green);
  }
  .brand__name {
    font-weight: 700; color: var(--ink);
    font-size: 34px; line-height: 1; letter-spacing: 1px;
    text-transform: uppercase;
  }
  .brand__name small { display: block; font-size: 16px; letter-spacing: 2px; margin-top: 6px; }

  .band {
    position: absolute; left: 0; right: 0; bottom: 0; height: 156px;
  }
  .band--green { background: var(--brand-green); }
  .band--dark { background: var(--brand-dark); }

  .person { position: absolute; left: 44px; top: 44px; color: var(--white); }
  .person__name { font-size: 19px; font-weight: 600; line-height: 24px; }
  .person__role { font-size: 15.5px; line-height: 20px; }

  .contacts { position: absolute; left: 256px; top: 27px; list-style: none; color: var(--white); font-size: 15.5px; }
  .contacts li { display: flex; align-items: center; gap: 9px; height: 20.5px; }
  .contacts svg { width: 12px; height: 12px; fill: var(--white); }

  .offer {
    position: absolute; left: 0; right: 0; top: 108px;
    text-align: center; color: var(--white); font-size: 15.5px; font-style: italic;
  }
  .offer strong { font-weight: 700; }

  .faint-brand {
    position: absolute; left: 120px; top: 72px;
    transform: scaleX(-1);
    opacity: 0.22;
  }

  .pitch { position: absolute; left: 0; right: 0; top: 16px; text-align: center; color: var(--white); }
  .pitch__title { font-size: 17.5px; font-weight: 600; line-height: 22px; margin-bottom: 8px; }
  .pitch__list { list-style: none; font-size: 16px; line-height: 20px; }
  .pitch__close { font-size: 15.5px; font-style: italic; margin-top: 10px; }
</style>
</head>
<body>
<main class="canvas">

  <section class="card card--front" aria-label="Business card front">
    <div class="brand">
      <span class="brand__dot"></span>
      <p class="brand__name">Lantern<small>Financial Coaching</small></p>
    </div>

    <div class="band band--green">
      <div class="person">
        <p class="person__name">Daniel R. Whitaker</p>
        <p class="person__role">Personal anancial coach</p>
      </div>
      <ul class="contacts">
        <li><svg viewBox="0 0 24 24" aria-hidden="true"><path d="M6.6 10.8a15.2 15.2 0 0 0 6.6 6.6l2.2-2.2a1 1 0 0 1 1-.25 11.4 11.4 0 0 0 3.6.57 1 1 0 0 1 1 1V20a1 1 0 0 1-1 1A17 17 0 0 1 3 4a1 1 0 0 1 1-1h3.5a1 1 0 0 1 1 1c0 1.25.2 2.45.57 3.6a1 1 0 0 1-.25 1z"/></svg>(555) 014-2290</li>
        <li><svg viewBox="0 0 24 24" aria-hidden="true"><path d="M3 5h18v14H3z M3 5l9 7 9-7" /></svg>daniel@steadyledgercoach.com</li>
        <li><svg viewBox="0 0 24 24" aria-hidden="true"><path d="M12 2a10 10 0 1 0 0 20 10 10 0 0 0 0-20zm-1 17.9A8 8 0 0 1 4.1 11H7l4 4zm6.9-2.6A2 2 0 0 0 16 16h-1v-3l-5-5h3V6h2a8 8 0 0 1 2.9 11.3z"/></svg>www.steadyledgercoach.com</li>
      </ul>
      <p class="offer"><strong>SPECIAL OFFER!:</strong> FREE 30 minute consultation</p>
    </div>
  </section>

  <section class="card card--back" aria-label="Business card back">
    <div class="brand faint-brand" aria-hidden="true">
      <span class="brand__dot"></span>
      <p class="brand__name">Lantern<small>Financial Coaching</small></p>
    </div>

    <div class="band band--dark">
      <div class="pitch">
        <p class="pitch__title">STRUGGLING WITH YOUR FINANCES?</p>
        <ul class="pitch__list">
          <li>Learn to become debt free</li>
          <li>Discover the power of cash</li>
          <li>Control your money instead of it controlling you</li>
        </ul>
        <p class="pitch__close">Let us help you achieve a new level of financial freedom!</p>
      </div>
    </div>
  </section>

</main>
</body>
</html>
```